Business Card Design For Financial Company

Create a new design for company's business card. The corporate logo is attached in several formats. Our new website design is also attached and we would like the business cards to reflect this.
Card needs to contain the following info:
Name
Job Title
Legal company name - eg Varomel Holdings (Asia) Ltd
Address - eg 517-09 Brellford Plaza,46 Tamsworth Lane, Hong Kong
Direct tel
Main tel
Fax
Email
Website URL
MS word format preferred. Other formats that can be edited on standard PC also OK.
Updates
Please note the the "VAROMEL" logo nameĀ font is "Gill Sans MT" on Windows
Target Market(s)
Instituation Investors
Industry/Entity Type
Business
Look and feel
Each slider illustrates characteristics of the customer's brand and the style your logo design should communicate.

```html
<!DOCTYPE html>
<html lang="en">
<head>
<meta charset="utf-8">
<title>Varomel Holdings – Business Card</title>
<link rel="stylesheet" href="https://fonts.googleapis.com/css2?family=Cabin:wght@400;700&display=swap">
<style>
  :root {
    --page: #ffffff;
    --card-light: #ffffff;
    --card-dark: #58585a;
    --ink: #5a5a5c;
    --ink-soft: #6b6b6d;
    --accent: #d41f26;
    --rule: #6b6b6d;
    --white: #ffffff;
  }
  * { margin: 0; padding: 0; box-sizing: border-box; }
  html, body {
    width: 1200px; height: 502px; overflow: hidden;
    background: var(--page);
    font-family: "Cabin", "Gill Sans", sans-serif;
  }
  .canvas { position: relative; width: 1200px; height: 502px; }
  .card {
    position: absolute; top: 111px;
    width: 487px; height: 286px;
    box-shadow: 0 1px 5px rgba(0,0,0,0.28);
  }
  .card--front { left: 83px; background: var(--card-light); }
  .card--back { left: 642px; background: var(--card-dark); }

  .brand-name {
    position: absolute; font-weight: 700; font-size: 28px; line-height: 1;
  }
  .legal-name {
    position: absolute; font-size: 14px; line-height: 1;
  }
  .card--front .brand-name { left: 40px; top: 76px; color: var(--ink); }
  .card--front .legal-name { left: 170px; top: 88px; color: var(--ink); }
  .brand-dot { position: absolute; left: 384px; top: 22px; }
  .rule {
    position: absolute; left: 20px; top: 111px;
    width: 446px; height: 2px; background: var(--rule);
  }
  .person-name {
    position: absolute; left: 40px; top: 126px;
    font-weight: 700; font-size: 20px; color: var(--accent);
  }
  .person-title {
    position: absolute; left: 40px; top: 150px;
    font-size: 16px; color: var(--accent);
  }
  .contact {
    position: absolute; top: 186px;
    font-size: 14.5px; line-height: 18px; color: var(--ink-soft);
    list-style: none;
  }
  .contact--phones { left: 40px; }
  .contact--address { left: 248px; }
  .label { color: var(--accent); }

  .card--back .brand-name { left: 98px; top: 120px; color: var(--white); }
  .card--back .legal-name { left: 242px; top: 132px; color: var(--white); }
  .back-dot { position: absolute; left: 40px; top: 112px; }
</style>
</head>
<body>
<main class="canvas">
  <section class="card card--front" aria-label="Business card front">
    <span class="brand-name">Varomel</span>
    <span class="legal-name">VAROMEL Holdings (Asia) Limited</span>
    <svg class="brand-dot" width="76" height="76" viewBox="0 0 76 76" aria-hidden="true">
      <circle cx="38" cy="38" r="38" fill="var(--accent)"/>
    </svg>
    <div class="rule"></div>
    <p class="person-name">Dumy Name</p>
    <p class="person-title">Dumy Title</p>
    <ul class="contact contact--phones">
      <li><span class="label">t:</span> +852 3961 2085</li>
      <li><span class="label">t:</span> +852 3961 2085</li>
      <li><span class="label">f:</span> +852 3961 2090</li>
      <li><span class="label">w:</span>www.varomelholdings.com</li>
    </ul>
    <ul class="contact contact--address">
      <li>517-09 Brellford Plaza 46</li>
      <li>Tamsworth Lane Hong Kong</li>
      <li><span class="label">e:</span> contact@varomelholdings.com</li>
    </ul>
  </section>

  <section class="card card--back" aria-label="Business card back">
    <svg class="back-dot" width="48" height="48" viewBox="0 0 48 48" aria-hidden="true">
      <circle cx="24" cy="24" r="24" fill="var(--white)"/>
    </svg>
    <span class="brand-name">Varomel</span>
    <span class="legal-name">VAROMEL Holdings (Asia) Limited</span>
  </section>
</main>
</body>
</html>
```